I need a website built for my modeling agency company.

On our website, a user can create a profile and we will submit it to thousands of modeling agents throughout the country.

In many cases, they will receive multiple offers from modeling agencies which allows them to pick and choose the contract that is best for them to launch their modeling career.

Some tag lines to consider using:

"Submit your profile to hundreds of modeling agents instantly!"

"Get found and become a star!"

We are: The Runway Guild.

Our Slogan: The World''s Largest Network of Fashion Models and Agents

What We Do: We are an agency with one of the largest networks of fashion professionals that are looking for new modeling talent. We host professional profiles for aspiring models, professional fashion models seeking work, modeling talent seekers, and top modeling agencies. We connect aspiring models with the top modeling agencies in the United States and abroad.

By submitting your FREE profile, you will be instantly introduced to the industry’s leading modeling agents. Within a few days, you could receive multiple, competing offers from modeling agencies that all want to launch your modeling career. Receiving multiple signing offers puts you in control of deciding which contract best suites you!

Reason: I've seen some good designs, but none that are 100% perfect. These are the ones that I like best so far (to give you some ideas): http://files.pixelvane.example/img/510372/820114/820114_4917263_510372_image.jpg http://files.pixelvane.example/img/510372/829305/829305_4926851_510372_image.jpg http://files.pixelvane.example/img/510372/51847/51847_4924097_510372_image.jpg http://files.pixelvane.example/img/510372/51847/51847_4919856_510372_image.jpg http://files.pixelvane.example/img/510372/823670/823670_4920438_510372_image.jpg

Target Market(s)

Aspiring models (mostly female, but some male)

Industry/Entity Type

Modeling Agency

Colors

Designer to choose colors to be used in the design.

Requirements
Nice to have
• Somewhere in the top half of the page, I would like there to be a small form for the visitor to fill out. This form will look as follows:

Title: Instantly contact hundreds of modeling agents who are looking for new talent and could make you a star!
Fields: First Name*, Last Name*, Age, Zip Code, Email Address*, Daytime Phone, Evening Phone, Comments.

Then, there will be a "submit" button to proceed to next step of form. Just below the "submit" button, should be the following verbiage: "You will have the opportunity to upload photo(s) and provide other pertinent information in next step."

```html
<!DOCTYPE html>
<html lang="en">
<head>
<meta charset="utf-8">
<title>The Runway Guild</title>
<link rel="stylesheet" href="https://fonts.googleapis.com/css2?family=Arimo:wght@400;700&display=swap">
<style>
:root{
  --ink:#222;
  --text:#333;
  --muted:#777;
  --rule:#dcdcdc;
  --magenta:#c8107c;
  --night:#000;
  --panel:#1b1b1b;
  --field-line:#6a6a6a;
  --label:#bdbdbd;
}
*{box-sizing:border-box;margin:0;padding:0}
html,body{width:820px;height:1200px;overflow:hidden;background:#fff}
body{position:relative;font-family:"Arimo",Helvetica,Arial,sans-serif;color:var(--text)}
a{color:inherit;text-decoration:none}
.abs{position:absolute}

/* top bar */
.topbar{left:0;top:0;width:820px;height:24px;background:var(--night)}
.topbar a{position:absolute;top:6px;font-size:11px;color:#cfcfcf;letter-spacing:.2px}

/* brand */
.brand{left:0;top:52px;width:820px;text-align:center}
.brand-name{display:inline-flex;align-items:center;gap:8px;font-size:25px;color:var(--ink);line-height:1}
.brand-mark{width:16px;height:16px;background:var(--magenta)}
.brand-slogan{font-size:8px;color:var(--ink);margin-top:8px;font-weight:700}

.rule{height:2px;background:var(--rule);left:78px;width:663px}

/* navigation */
.main-nav a,.footer-nav a{position:absolute;font-size:11px;letter-spacing:.2px}
.main-nav a{top:140px;color:var(--text)}
.plus{color:var(--magenta)}

/* hero */
.hero-side{left:0;top:164px;width:75px;height:323px;background:linear-gradient(160deg,#3a3a3a,#151515)}
.hero-photo{left:78px;top:164px;width:419px;height:323px;background:linear-gradient(90deg,#e6e6e6 0%,#cfcfcf 45%,#8a8a8a 60%,#e3e3e3 100%)}
.signup{left:500px;top:164px;width:320px;height:323px;background:linear-gradient(120deg,#121212 0%,#2a2a2a 55%,#191919 100%)}
.signup-title{position:absolute;left:20px;top:22px;font-size:11.5px;line-height:12px;color:#c9c9c9}
.signup-title .strong{color:#fff}
.signup-title .accent{color:var(--magenta)}
.field-label{position:absolute;font-size:7px;color:var(--label);letter-spacing:.2px}
.field{position:absolute;height:14px;border:1px solid var(--field-line);background:rgba(0,0,0,.25)}
.submit{position:absolute;left:95px;top:254px;width:51px;height:18px;background:var(--magenta);color:#fff;font-size:11px;text-align:center;line-height:18px}
.signup-note{position:absolute;left:20px;top:287px;font-size:6.5px;line-height:9px;color:#f0f0f0}

/* intro */
.intro{left:0;top:505px;width:820px;text-align:center}
.intro h1{font-size:11px;font-weight:400;color:var(--magenta);margin-bottom:13px}
.intro p{font-size:10px;line-height:12.3px;color:var(--text);margin-bottom:12px}

/* section headers */
.section-title{font-size:11px;color:var(--ink)}
.see-more{font-size:11px;color:var(--muted)}
.see-more b{color:var(--magenta);font-size:14px;margin-left:4px}

/* carousel */
.carousel{left:79px;top:672px;width:662px;height:160px;display:flex}
.carousel .tile{flex:1}
.scrollbar{left:78px;top:838px;width:663px;height:9px}

/* columns */
.post{position:absolute;width:198px;height:48px}
.post .thumb{position:absolute;left:0;top:0;width:40px;height:40px;background:linear-gradient(135deg,#d8c3ac,#7b6553)}
.post .excerpt{position:absolute;left:45px;top:-1px;font-size:9px;line-height:11.5px;color:var(--ink)}
.post .date{position:absolute;left:45px;top:34px;font-size:7px;color:var(--muted)}
.divider{position:absolute;height:1px;background:var(--rule);width:198px}
.press-photo{left:535px;top:896px;width:206px;height:182px;background:linear-gradient(180deg,#d4d6da,#a9abb3)}

/* social & footer */
.social{left:0;top:1135px;width:820px;height:16px}
.footer{left:0;top:1162px;width:820px;height:38px;background:var(--magenta)}
.footer-nav a{top:7px;color:#fff}
</style>
</head>
<body>

<header>
  <div class="abs topbar">
    <a href="#" style="left:621px">SIGN UN</a>
    <a href="#" style="left:692px">LOG IN</a>
  </div>

  <div class="abs brand">
    <div class="brand-name"><span class="brand-mark"></span>The Runway Guild</div>
    <div class="brand-slogan">The World's Largest Network of Fashion Models and Agents</div>
  </div>

  <div class="abs rule" style="top:127px"></div>

  <nav class="main-nav">
    <a href="#" style="left:249px">HOME</a>
    <a href="#" style="left:310px"><span class="plus">+</span> ABOUT</a>
    <a href="#" style="left:382px"><span class="plus">+</span> MODELS</a>
    <a href="#" style="left:463px">NEWS</a>
    <a href="#" style="left:523px">CONTACT</a>
  </nav>
</header>

<section class="hero">
  <div class="abs hero-side" role="img" aria-label="Dark textured fashion photograph"></div>
  <div class="abs hero-photo" role="img" aria-label="Black and white portrait of a model with long straight blonde hair"></div>

  <form class="abs signup" aria-label="Model sign-up">
    <div class="signup-title">
      INSTANTLY CONTACT<br>
      <span class="strong">HUNDREDS OF MODELING AGENTS</span><br>
      WHO ARE LOOKING FOR NEW TALENT<br>
      <span class="accent">AND COULD MAKE YOU A STAR!</span>
    </div>

    <span class="field-label" style="left:21px;top:87px">FIRST NAME*</span>
    <span class="field-label" style="left:98px;top:87px">LAST NAME*</span>
    <span class="field" style="left:20px;top:96px;width:72px"></span>
    <span class="field" style="left:97px;top:96px;width:123px"></span>

    <span class="field-label" style="left:21px;top:115px">AGE</span>
    <span class="field-label" style="left:98px;top:115px">ZIP CODE</span>
    <span class="field" style="left:20px;top:124px;width:72px"></span>
    <span class="field" style="left:97px;top:124px;width:123px"></span>

    <span class="field-label" style="left:21px;top:143px">EMAIL</span>
    <span class="field" style="left:20px;top:152px;width:200px"></span>

    <span class="field-label" style="left:21px;top:169px">DAYTIME PHONE</span>
    <span class="field-label" style="left:124px;top:169px">EVENING PHONE</span>
    <span class="field" style="left:20px;top:178px;width:100px"></span>
    <span class="field" style="left:124px;top:178px;width:96px"></span>

    <span class="field-label" style="left:21px;top:197px">COMMENTS</span>
    <span class="field" style="left:20px;top:206px;width:200px;height:41px"></span>

    <span class="submit">SUBMIT</span>

    <p class="signup-note">YOU WILL HAVE THE OPPORTUNITY TO UPLOAD PHOTO(S) AND<br>PROVIDE OTHER PERTINENT INFORMATION IN NEXT STEP</p>
  </form>
</section>

<section class="abs intro">
  <h1>SUBMIT YOUR PROFILE TO HUNDREDS OF MODELING AGENTS INSTANTLY!</h1>
  <p>We are an agency with one of the largest networks of fashion professionals that are looking for new modeling talent.<br>
  We host professional profiles for aspiring models, professional fashion models seeking work, modeling talent seekers, and top modeling agencies.<br>
  We connect aspiring models with the top modeling agencies in the United States and abroad.</p>
  <p>By submitting your FREE profile, you will be instantly introduced to the industry's leading modeling agents.<br>
  Within a few days, you could receive multiple, competing offers from modeling agencies that all want to launch your modeling career.<br>
  Receiving multiple signing offers puts you in control of deciding which contract best suites you!</p>
</section>

<div class="abs rule" style="top:638px;height:1px"></div>

<section class="latest-models">
  <h2 class="abs section-title" style="left:78px;top:655px;font-weight:400">LATEST MODELS</h2>
  <a class="abs see-more" href="#" style="left:671px;top:653px">SEE MORE<b>»</b></a>

  <div class="abs carousel">
    <div class="tile" role="img" aria-label="Model with long blonde hair" style="background:linear-gradient(135deg,#f1e6cf,#c9a66e)"></div>
    <div class="tile" role="img" aria-label="Model in a plaid cap with auburn hair" style="background:linear-gradient(135deg,#e8dcc6,#7a4a3c)"></div>
    <div class="tile" role="img" aria-label="Close-up of a model with wavy blonde hair" style="background:linear-gradient(135deg,#b48a6a,#5d3f2f)"></div>
    <div class="tile" role="img" aria-label="Male model in a striped jacket" style="background:linear-gradient(135deg,#d9d9d9,#6e6e6e)"></div>
  </div>

  <svg class="abs scrollbar" width="663" height="9" viewBox="0 0 663 9">
    <rect x="0" y="0" width="9" height="9" fill="#8a8a8a"/>
    <path d="M6 2 L3 4.5 L6 7Z" fill="#fff"/>
    <rect x="9" y="3" width="645" height="3" fill="#d8d8d8"/>
    <rect x="23" y="2" width="38" height="5" fill="#7a7a7a"/>
    <rect x="654" y="0" width="9" height="9" fill="#8a8a8a"/>
    <path d="M657 2 L660 4.5 L657 7Z" fill="#fff"/>
  </svg>
</section>

<div class="abs rule" style="top:866px;height:1px"></div>

<section class="columns">
  <h2 class="abs section-title" style="left:78px;top:877px;font-weight:400">NEWS</h2>
  <h2 class="abs section-title" style="left:308px;top:877px;font-weight:400">TESTIMONIALS</h2>
  <h2 class="abs section-title" style="left:535px;top:877px;font-weight:400">PRESS</h2>

  <!-- news -->
  <article class="post" style="left:78px;top:897px"><div class="thumb" role="img" aria-label="Model portrait thumbnail"></div><p class="excerpt">Lorem Ipsum is simply dummy text of<br>the printing and typesetting industry.</p><span class="date">Posted: Nov 26th</span></article>
  <div class="divider" style="left:78px;top:946px"></div>
  <article class="post" style="left:78px;top:962px"><div class="thumb" role="img" aria-label="Model portrait thumbnail"></div><p class="excerpt">Lorem Ipsum is simply dummy text of<br>the printing and typesetting industry.</p><span class="date">Posted: Nov 26th</span></article>
  <div class="divider" style="left:78px;top:1015px"></div>
  <article class="post" style="left:78px;top:1027px"><div class="thumb" role="img" aria-label="Model portrait thumbnail"></div><p class="excerpt">Lorem Ipsum is simply dummy text of<br>the printing and typesetting industry.</p><span class="date">Posted: Nov 26th</span></article>
  <div class="divider" style="left:78px;top:1078px"></div>
  <a class="abs see-more" href="#" style="left:203px;top:1084px">SEE MORE<b>»</b></a>

  <!-- testimonials -->
  <article class="post" style="left:308px;top:897px"><div class="thumb" role="img" aria-label="Model portrait thumbnail"></div><p class="excerpt">Lorem Ipsum is simply dummy text of<br>the printing and typesetting industry.</p><span class="date">Posted: Nov 26th</span></article>
  <div class="divider" style="left:308px;top:946px"></div>
  <article class="post" style="left:308px;top:962px"><div class="thumb" role="img" aria-label="Model portrait thumbnail"></div><p class="excerpt">Lorem Ipsum is simply dummy text of<br>the printing and typesetting industry.</p><span class="date">Posted: Nov 26th</span></article>
  <div class="divider" style="left:308px;top:1015px"></div>
  <article class="post" style="left:308px;top:1027px"><div class="thumb" role="img" aria-label="Model portrait thumbnail"></div><p class="excerpt">Lorem Ipsum is simply dummy text of<br>the printing and typesetting industry.</p><span class="date">Posted: Nov 26th</span></article>
  <div class="divider" style="left:308px;top:1078px"></div>
  <a class="abs see-more" href="#" style="left:435px;top:1084px">SEE MORE<b>»</b></a>

  <!-- press -->
  <div class="abs press-photo" role="img" aria-label="Full-length model in a dark metallic coat"></div>
  <a class="abs see-more" href="#" style="left:671px;top:1084px">SEE MORE<b>»</b></a>
</section>

<div class="abs rule" style="top:1125px;height:1px"></div>

<svg class="abs social" width="820" height="16" viewBox="0 0 820 16" aria-label="Social links">
  <circle cx="389" cy="8" r="7.5" fill="#666"/>
  <circle cx="411" cy="8" r="7.5" fill="#444"/>
  <circle cx="433" cy="8" r="7.5" fill="#555"/>
  <circle cx="455" cy="8" r="7.5" fill="#777"/>
</svg>

<footer class="abs footer">
  <nav class="footer-nav">
    <a href="#" style="left:249px">HOME</a>
    <a href="#" style="left:310px">+ ABOUT</a>
    <a href="#" style="left:382px">+ MODELS</a>
    <a href="#" style="left:463px">NEWS</a>
    <a href="#" style="left:523px">CONTACT</a>
  </nav>
</footer>

</body>
</html>
```